LITTLE DESIGN WORK REQUIRED!

UPDATE: WE WEREN'T OVERLY ECSTATIC WITH THE DESIGNS WE WERE RECEIVING SO WE DID MOST OF THE DESIGN WORK OURSELVES...

PLEASE SEE THE NEWLY ATTACHED PPT DOC TO VIEW NEARLY EXACT REPLICAS OF WHAT WE WANT THE SITE TO LOOK LIKE. WE NOW NEED YOUR HELP TO MAKE IT LOOK LIKE SOMETHING WORTHY OF THE WEB.

NO CODING REQUIRED - EXPECTED OUTPUT PSD FILES

Hi everyone!

We're looking for a designer to work their magic for our site! We're a not-for-profit program aimed at helping young people realise their potential!

In the attached PPT file, you'll notice we've already DESIGNED THE ENTIRE SITE IN POWERPOINT. Now, we need YOU to make the small changes we requested in the document as well as design the whole thing in psd.

Any questions, don't hesitate to ask.

Brook-Rise
Updates

We've done about 95% of the design for you. Please fine-tune it. See the newly attached PPT doc for details. 

The best two designs will win. This project closes on Friday - please message us if you are absolutely sure you cannot make the deadline.

Thanks,
Brook-Rise

```html
<!DOCTYPE html>
<html lang="en">
<head>
<meta charset="utf-8">
<title>Brook-Rise – About Us</title>
<link href="https://fonts.googleapis.com/css2?family=PT+Sans:wght@400;700&family=Arimo:wght@400;700&display=swap" rel="stylesheet">
<style>
:root{
  --green:#7dbb0e;
  --green-dark:#5f9a05;
  --blue:#1a8ccc;
  --blue-light:#45a2d8;
  --ink:#3a3a3a;
  --body:#4a4a4a;
  --nav-top:#4a4a4a;
  --nav-bottom:#1c1c1c;
  --line:#dcdcdc;
  --white:#ffffff;
}
*{margin:0;padding:0;box-sizing:border-box}
html,body{width:1200px;height:867px;overflow:hidden;background:var(--white)}
body{position:relative;font-family:"Arimo",Arial,sans-serif;color:var(--body)}
.page-top{position:absolute;left:0;top:0;width:1200px;height:30px;background:linear-gradient(#ececec,#fff)}
.brand{position:absolute;display:flex;align-items:center;gap:10px;font-family:"PT Sans",sans-serif;font-weight:700;color:#1e1e1e}
.brand-mark{width:26px;height:26px;border-radius:50%;background:var(--green)}
.brand--header{left:112px;top:44px;font-size:40px}
.brand--footer{left:112px;top:757px;font-size:32px}
.contact-card{position:absolute;left:752px;top:23px;width:337px;height:85px;border:2px solid #eee;border-radius:3px;background:#fff;font-family:"PT Sans",sans-serif;font-weight:700;font-size:18px;color:#555}
.contact-card .icon{position:absolute;left:6px;top:14px}
.contact-card .email{position:absolute;left:66px;top:17px}
.contact-card .phone{position:absolute;left:66px;top:47px}
.contact-card .accent{color:var(--green)}
.main-nav{position:absolute;left:110px;top:131px;width:980px;height:44px;border-radius:4px;background:linear-gradient(var(--nav-top),#2a2a2a 50%,var(--nav-bottom));box-shadow:0 3px 4px rgba(0,0,0,.25);display:flex}
.main-nav a{display:block;height:44px;line-height:46px;text-align:center;color:#fff;font-size:13px;text-decoration:none;border-right:1px solid #555}
.main-nav a.is-active{background:linear-gradient(#8fcf1c,var(--green-dark))}
.search{position:absolute;right:12px;top:10px;width:195px;height:25px;border-radius:13px;background:linear-gradient(#777,#555);box-shadow:inset 0 1px 2px rgba(0,0,0,.4);color:#eee;font-size:12px;line-height:25px;padding-left:21px}
.search svg{position:absolute;right:9px;top:5px}
.page-title{position:absolute;left:109px;top:202px;font-family:"PT Sans",sans-serif;font-weight:400;font-size:30px;color:var(--ink)}
.section-title{position:absolute;left:111px;font-size:18px;font-weight:400;color:var(--blue)}
.copy{position:absolute;left:114px;width:970px;font-size:12px;line-height:18px;color:var(--body)}
.framework{position:absolute;left:175px;top:567px}
.framework text{font-family:"Arimo",Arial,sans-serif;font-size:17px;fill:#fff}
.footer{position:absolute;left:0;top:686px;width:1200px;height:181px;background:linear-gradient(#d8d8d8,#fff 22px)}
.copyright{position:absolute;left:112px;top:708px;font-size:11px;color:#222}
.contact-form{position:absolute;left:549px;top:706px;width:541px;height:142px;border:1px solid #e0e0e0;border-radius:5px;background:linear-gradient(#fff,#ececec);overflow:hidden}
.form-label-panel{position:absolute;left:0;top:0;width:109px;height:142px;background:var(--green);color:#fff;font-size:18px;line-height:24px;text-align:center;padding-top:14px}
.form-label-panel svg{display:block;margin:8px auto 0}
.field-label{position:absolute;left:139px;font-size:12px;font-weight:700;color:#333}
.field{position:absolute;left:251px;width:156px;height:26px;border:1px solid #ccc;background:#fff;box-shadow:inset 0 1px 2px rgba(0,0,0,.1)}
.submit{position:absolute;left:417px;top:84px;width:91px;height:43px;border-radius:4px;border:1px solid var(--green-dark);background:linear-gradient(#a6dc3c,var(--green-dark));color:#fff;font-size:13px;font-weight:700;text-align:center;line-height:41px;box-shadow:inset 0 0 0 2px rgba(255,255,255,.35)}
</style>
</head>
<body>
<div class="page-top"></div>

<div class="brand brand--header"><span class="brand-mark"></span>BROOK-RISE</div>

<div class="contact-card">
  <svg class="icon" width="52" height="60" viewBox="0 0 52 60" aria-hidden="true">
    <circle cx="24" cy="16" r="12" fill="#2db0e8"/>
    <path d="M2 56 Q4 32 24 32 Q44 32 46 56 Z" fill="#2db0e8"/>
    <circle cx="40" cy="44" r="9" fill="#fff" stroke="#2db0e8" stroke-width="2"/>
    <path d="M36 40 l2 0 l1 3 l-1 1 q1 2 3 3 l1-1 l3 1 l0 2 q-5 1 -9-9z" fill="#2db0e8"/>
  </svg>
  <div class="email">Email : <span class="accent">hello@brookrise.org</span></div>
  <div class="phone">Call us on : +44 (0) 1632 960 418</div>
</div>

<nav class="main-nav">
  <a href="#" style="width:95px">Home</a>
  <a href="#" class="is-active" style="width:97px">About Us</a>
  <a href="#" style="width:113px">Resources</a>
  <a href="#" style="width:110px">Workshops</a>
  <a href="#" style="width:134px">Ambassadors</a>
  <a href="#" style="width:96px">Feats</a>
  <div class="search">Enter Keyword
    <svg width="16" height="16" viewBox="0 0 16 16" aria-hidden="true"><circle cx="6.5" cy="6.5" r="4.5" fill="none" stroke="#fff" stroke-width="2"/><line x1="10" y1="10" x2="14" y2="14" stroke="#fff" stroke-width="2.4"/></svg>
  </div>
</nav>

<h1 class="page-title">About Us</h1>

<h2 class="section-title" style="top:259px">The Situation</h2>
<p class="copy" style="top:292px">The gap between what we can achieve and what we do achieve is bigger than ever. This unrealised potential could arguably be the most common commodity on earth, but unlike other commodities, it can't be shared, it can't be traded, and it can't be bought – so when it goes unused, it simply goes to waste. All too often this happens: people wander aimlessly without goals or a direction in mind, they get stuck in a state of comfort, and they resign to mediocrity – but just imagine the possibilities if this potential were unlocked..</p>

<h2 class="section-title" style="top:362px">What we do</h2>
<p class="copy" style="top:395px">Brook-Rise is a not-for-profit program aimed at helping people – especially young people – realise their potential and achieve success. We understand that achievement can be measured in any number of ways and that success is entirely unique to the individual who defines it. But we also believe that – no matter how unique success may be – it's powered by a single, common framework that, if taught effectively, can be followed by anyone.</p>
<p class="copy" style="top:467px">This framework is at the centre of everything we offer at Brook-Rise, from our online resources and in-school workshops, to our ambassadors' network and Brook-Rise feats projects. So what's the end result? Simple. You'll Brook-Rise your life, reach your potential, and who knows… maybe even change the world.</p>

<h2 class="section-title" style="top:522px">The Framework</h2>

<svg class="framework" width="880" height="78" viewBox="0 0 880 78" aria-label="Framework steps: Discover, Design, Build, Achieve">
  <defs>
    <linearGradient id="chev" x1="0" y1="0" x2="0" y2="1">
      <stop offset="0" stop-color="#45a2d8"/><stop offset=".5" stop-color="#45a2d8"/>
      <stop offset=".5" stop-color="#1a8ccc"/><stop offset="1" stop-color="#1a8ccc"/>
    </linearGradient>
  </defs>
  <path d="M0 0 H200 L222 38 L200 76 H0 Z" fill="url(#chev)"/>
  <path d="M219 0 H420 L442 38 L420 76 H219 L241 38 Z" fill="url(#chev)"/>
  <path d="M438 0 H638 L660 38 L638 76 H438 L460 38 Z" fill="url(#chev)"/>
  <path d="M655 0 H857 L879 38 L857 76 H655 L677 38 Z" fill="url(#chev)"/>
  <text x="108" y="46" text-anchor="middle">Discover</text>
  <text x="337" y="46" text-anchor="middle">Design</text>
  <text x="556" y="46" text-anchor="middle">Build</text>
  <text x="770" y="46" text-anchor="middle">Achieve</text>
</svg>

<footer class="footer"></footer>
<p class="copyright">Copyright © 2012 brookrise. All Rights Reserved</p>
<div class="brand brand--footer"><span class="brand-mark"></span>BROOK-RISE</div>

<form class="contact-form">
  <div class="form-label-panel">CONTACT<br>FORM
    <svg width="62" height="54" viewBox="0 0 62 54" aria-hidden="true">
      <rect x="14" y="2" width="46" height="34" rx="3" fill="#eef3f6" stroke="#9fb0ba"/>
      <rect x="2" y="14" width="46" height="34" rx="3" fill="#fff" stroke="#9fb0ba"/>
      <rect x="7" y="20" width="12" height="14" fill="#5aa0d8"/>
      <rect x="23" y="21" width="20" height="3" fill="#7b8b96"/>
      <rect x="23" y="28" width="20" height="3" fill="#7b8b96"/>
      <rect x="7" y="38" width="36" height="3" fill="#7b8b96"/>
    </svg>
  </div>
  <span class="field-label" style="top:20px">Full Name :</span>
  <span class="field-label" style="top:55px;left:140px">Email Address :</span>
  <span class="field-label" style="top:90px">Subject :</span>
  <span class="field" style="top:13px"></span>
  <span class="field" style="top:48px"></span>
  <span class="field" style="top:84px;height:43px"></span>
  <span class="submit">Submit</span>
</form>
</body>
</html>
```